Keelstone Advisory - Careerloom Header

I am a solopreneur with a consulting company. I do management consulting for small and mid-size manufacturers. There are two ways my prospects check me out - my web page, which went live this week (www.keelstoneadvisory.example), and my personal Careerloom page. I'm working on my Careerloom page now, and I'd like to have a header image that is unique and aligned with my brand.

My clients are smaller manufacturers, typically with 50-400 people. They are privately held, often by an individual or family, but sometimes by a professional investment group. They aren't as sophisticated as the Corvane 300 guys, and sometimes they struggle to grow because their processes break, or they don't have the right people or something else like that. I help them get through those issues.

Many of the people visiting the site will have a technical/engineering orientation, and most are in their late 40's to early 60's.

From my research, I think the image for my personal page is 1584x396, and this will be my primary page. The business page has a banner image size of 1536x768. I'd like to be able to use the same image in both.

Target Market(s)

Small and Mid-size manufacturers - C-Suite executives

Industry/Entity Type

Manufacturing

Font styles to use
Sans Serif

Colors

Designer to choose colors to be used in the design.

Requirements
Must have
• Logo incorporated. Be adaptable to both my personal Careerloom page and Business page, which have slightly different sizes.

```html
<!DOCTYPE html>
<html lang="en">
<head>
<meta charset="utf-8">
<title>Keelstone Advisory – Careerloom Header</title>
<link rel="stylesheet" href="https://fonts.googleapis.com/css2?family=Montserrat:wght@600;700&display=swap">
<style>
  :root {
    --navy-deep: #0a1a4f;
    --navy: #142c6e;
    --blue-mid: #2f4f95;
    --blue-soft: #5a78b4;
    --panel-tint: rgba(226, 232, 242, 0.82);
    --brand-ink: #2a3370;
    --glow: #2b3fd6;
    --white: #ffffff;
  }
  * { margin: 0; padding: 0; box-sizing: border-box; }
  html, body {
    width: 1200px; height: 300px; overflow: hidden;
    background: var(--navy-deep);
  }
  .header {
    position: relative;
    width: 1200px; height: 300px;
    overflow: hidden;
    font-family: "Montserrat", sans-serif;
  }
  .header__photo {
    position: absolute; inset: 0;
    background:
      radial-gradient(ellipse at 30% 75%, rgba(120, 150, 205, 0.55), transparent 45%),
      radial-gradient(ellipse at 62% 78%, rgba(95, 125, 185, 0.5), transparent 40%),
      linear-gradient(100deg, var(--blue-soft) 0%, var(--blue-mid) 30%, var(--navy) 60%, var(--navy-deep) 100%);
  }
  .header__overlay {
    position: absolute; inset: 0;
    background: linear-gradient(180deg, rgba(10, 26, 79, 0.35), rgba(10, 26, 79, 0.15));
  }
  .brand-panel {
    position: absolute; top: 0; left: 0;
    width: 192px; height: 300px;
    background: var(--panel-tint);
    display: flex; flex-direction: column; align-items: center;
    padding-top: 22px;
  }
  .brand-panel__mark {
    width: 40px; height: 40px; border-radius: 50%;
    background: var(--brand-ink);
    margin-bottom: 14px;
  }
  .brand-panel__name {
    color: var(--brand-ink);
    font-weight: 700;
    font-size: 21px;
    line-height: 1.15;
    text-align: center;
    letter-spacing: 0.3px;
  }
  .headline {
    position: absolute; top: 32px; left: 346px;
    width: 698px; height: 42px;
    display: flex; align-items: center; justify-content: center;
    background: var(--navy-deep);
    border-radius: 14px;
    box-shadow: 0 0 10px 4px var(--glow), 0 0 22px 8px rgba(43, 63, 214, 0.45);
  }
  .headline__text {
    color: var(--white);
    font-weight: 700;
    font-size: 30px;
    letter-spacing: 0.2px;
    white-space: nowrap;
  }
  .intro {
    position: absolute; top: 101px; left: 272px;
    width: 850px;
    color: var(--white);
    font-weight: 600;
    font-size: 14.5px;
    line-height: 24px;
    text-align: center;
  }
</style>
</head>
<body>
  <header class="header">
    <div class="header__photo" role="img" aria-label="Photo of business people reviewing a tablet with a pen across a meeting table, tinted blue"></div>
    <div class="header__overlay"></div>

    <div class="brand-panel">
      <span class="brand-panel__mark"></span>
      <p class="brand-panel__name">Keelstone<br>Advisory</p>
    </div>

    <div class="headline">
      <h1 class="headline__text">Enabling Manufacturers to Break Through</h1>
    </div>

    <p class="intro">Keelstone Advisory specializes in helping small- and mid-sized manufacturers to break through to<br>new levels of growth, scalability and financial performance.</p>
  </header>
</body>
</html>
```